Harbor Lantern Diagnostics
Stationary/Business Card
Project: Harbor Lantern Diagnostics
Harbor Lantern Diagnostics - Medical
Creative Brief
Use specific fonts
Font like in the uploaded pic (playing card)
Cutting-Edge
Marlo Quist
Chief Executive Officer
417 W Dunmore Ave, Fairhaven, OR
marlo_047@quillpost.example
harborlanterndiagnostics.example
For the stationary I uploaded some ideas of how I would love for it to look like.
For the front and the back design of the business card, I have uploaded
orvell512 orvell512
I've already picked the winner for the logo but I'm still waiting on the finished product from the designer.

```html
<!DOCTYPE html>
<html lang="en">
<head>
<meta charset="utf-8">
<title>Harbor Lantern Diagnostics – Business Card</title>
<link rel="stylesheet" href="https://fonts.googleapis.com/css2?family=Cinzel:wght@500;700&family=Lato:wght@400;700&display=swap">
<style>
  :root {
    --backdrop: #e9e4da;
    --card: #ffffff;
    --crimson: #8e1a16;
    --gold-light: #f2c75a;
    --gold-deep: #c98f1c;
    --ink: #5a1410;
  }
  * { margin: 0; padding: 0; box-sizing: border-box; }
  html, body {
    width: 1200px; height: 982px; overflow: hidden;
    background: var(--backdrop);
  }
  .canvas {
    position: relative; width: 1200px; height: 982px;
    display: flex; flex-direction: column; align-items: center; justify-content: center; gap: 44px;
  }
  .card {
    position: relative; width: 780px; height: 446px;
    background: var(--card);
    box-shadow: 0 6px 18px rgba(60, 40, 20, 0.18);
    overflow: hidden;
  }
  .card-art { position: absolute; inset: 0; }
  .brand {
    position: absolute; display: flex; flex-direction: column; align-items: center; gap: 18px;
  }
  .brand-mark {
    width: 92px; height: 92px; border-radius: 50%;
    background: var(--crimson);
  }
  .brand-name {
    font-family: "Cinzel", serif; font-weight: 500;
    font-size: 24px; letter-spacing: 2px; color: var(--crimson);
    text-align: center; line-height: 1.3;
  }
  .front .brand { left: 40px; top: 120px; width: 300px; }
  .back .brand { left: 0; right: 0; top: 130px; }
  .back .brand-name { font-size: 30px; }
  .details {
    position: absolute; left: 440px; top: 110px; width: 320px;
    font-family: "Lato", sans-serif; color: var(--ink);
  }
  .person-name {
    font-family: "Cinzel", serif; font-weight: 700;
    font-size: 26px; letter-spacing: 1.5px; color: var(--crimson);
  }
  .person-title {
    font-size: 15px; letter-spacing: 1px; margin-top: 4px; color: var(--ink);
  }
  .contact-list { list-style: none; margin-top: 40px; display: flex; flex-direction: column; gap: 12px; }
  .contact-item { display: flex; align-items: center; gap: 10px; font-size: 14px; white-space: nowrap; }
  .contact-icon { width: 16px; height: 16px; flex: none; fill: var(--crimson); }
</style>
</head>
<body>
<main class="canvas">

  <section class="card front" aria-label="Business card front">
    <svg class="card-art" viewBox="0 0 780 446" width="780" height="446" aria-hidden="true">
      <defs>
        <linearGradient id="goldFill" x1="0" y1="0" x2="1" y2="1">
          <stop offset="0" stop-color="#f2c75a"/>
          <stop offset="1" stop-color="#c98f1c"/>
        </linearGradient>
      </defs>
      <path d="M400 0 C 360 150, 400 300, 330 446 L780 446 L780 0 Z" fill="url(#goldFill)"/>
      <path d="M384 0 C 344 150, 384 300, 314 446" fill="none" stroke="#8e1a16" stroke-width="12"/>
    </svg>

    <div class="brand">
      <span class="brand-mark"></span>
      <span class="brand-name">Harbor Lantern<br>Diagnostics</span>
    </div>

    <div class="details">
      <div class="person-name">Marlo Quist</div>
      <div class="person-title">Chief Executive Officer</div>
      <ul class="contact-list">
        <li class="contact-item">
          <svg class="contact-icon" viewBox="0 0 16 16"><path d="M8 0a5 5 0 0 0-5 5c0 4 5 11 5 11s5-7 5-11a5 5 0 0 0-5-5zm0 7a2 2 0 1 1 0-4 2 2 0 0 1 0 4z"/></svg>
          417 W Dunmore Ave, Fairhaven, OR
        </li>
        <li class="contact-item">
          <svg class="contact-icon" viewBox="0 0 16 16"><path d="M3 1l3 3-1.5 2a9 9 0 0 0 5.5 5.5L12 10l3 3-2 2C7 15 1 9 1 3z"/></svg>
          (555) 010-4421
        </li>
        <li class="contact-item">
          <svg class="contact-icon" viewBox="0 0 16 16"><path d="M1 3h14v10H1zM2 4l6 5 6-5v1L8 10 2 5z"/></svg>
          marlo_047@quillpost.example
        </li>
        <li class="contact-item">
          <svg class="contact-icon" viewBox="0 0 16 16"><circle cx="8" cy="8" r="7" fill="none" stroke="#8e1a16" stroke-width="1.5"/><path d="M1 8h14M8 1c3 3 3 11 0 14M8 1c-3 3-3 11 0 14" fill="none" stroke="#8e1a16" stroke-width="1.2"/></svg>
          harborlanterndiagnostics.example
        </li>
      </ul>
    </div>
  </section>

  <section class="card back" aria-label="Business card back">
    <div class="brand">
      <span class="brand-mark"></span>
      <span class="brand-name">Harbor Lantern Diagnostics</span>
    </div>
  </section>

</main>
</body>
</html>
```